Microsoft Word Template for 1, 2, and 4-page quick hit, topical pieces

I am looking for someone to create a professional and dynamic Microsoft Word Template that will allow us to easily add content to produce brochures and whitepapers on various topics. We'd like the template to be 4 pages with the idea that we may use all or just 1-2 of the pages in a brochure. We are fond of bold color, white space, and a good ratio of text to graphics. We have a large catalog of stock images so placeholders for photographs can be included if it fits the design. There is the possibility of expanded design opportunities in the future. I have attached our logo and colors.

Target Market(s)

Libraries - Public, Government, Higher Education, and Corporate

Font styles to use
Serif
Sans Serif

Requirements
Must have
• Editable Word Template that has 4 variable but cohesively designed pages. Use our logo and colors (see uploaded documents)
Nice to have
• Lots of white space, spaces for photos and graphics, spaces for blocks of text. Color.
Should not have
• Giant blocks of text. The exact same frame (header and footer) on each page.

```html
<!DOCTYPE html>
<html lang="en">
<head>
<meta charset="utf-8">
<title>Lumenora Brochure Template</title>
<link rel="stylesheet" href="https://fonts.googleapis.com/css2?family=Arimo:wght@400;700&display=swap">
<style>
  :root {
    --canvas: #f8f6f7;
    --paper: #ffffff;
    --olive: #a0a81b;
    --olive-dark: #8c9418;
    --forest: #1d5a30;
    --forest-deep: #245c36;
    --forest-soft: #6a9474;
    --panel-green: #41583d;
    --earth: #6b5c48;
    --ink: #1b1b1b;
    --white: #ffffff;
  }
  * { margin: 0; padding: 0; box-sizing: border-box; }
  html, body { width: 884px; height: 1200px; overflow: hidden; background: var(--canvas); }
  body { position: relative; font-family: "Arimo", Arial, sans-serif; color: var(--ink); }

  .backdrop { position: absolute; left: 100px; top: 139px; width: 684px; height: 920px; background: var(--paper); }

  .page { position: absolute; width: 378px; height: 537px; overflow: hidden; background: var(--paper); }
  .page--cover { left: 32px; top: 32px; }
  .page--inside-a { left: 474px; top: 32px; }
  .page--inside-b { left: 32px; top: 632px; }
  .page--back { left: 474px; top: 632px; background: var(--forest-deep); }
  .page svg.art { position: absolute; left: 0; top: 0; width: 378px; height: 537px; }

  .brand { position: absolute; display: flex; align-items: center; gap: 4px; color: var(--white); font-weight: 400; font-size: 16px; letter-spacing: -0.2px; }
  .brand__dot { width: 16px; height: 16px; border-radius: 50%; border: 1.5px solid var(--white); }

  /* cover */
  .cover-title { position: absolute; left: 18px; top: 98px; color: var(--white); font-weight: 700; line-height: 1; }
  .cover-title__main { display: block; font-size: 48px; letter-spacing: 1px; }
  .cover-title__sub { display: block; font-size: 26px; margin-top: 6px; letter-spacing: 1px; margin-left: 2px; }
  .cover-intro { position: absolute; left: 107px; top: 245px; width: 260px; color: var(--white); font-size: 10px; line-height: 14.5px; letter-spacing: 0.6px; }
  .page--cover .brand { left: 20px; top: 494px; }

  /* inside */
  .section-title { position: absolute; left: 44px; top: 23px; color: var(--white); font-weight: 700; font-size: 17px; letter-spacing: 0.6px; }
  .columns { position: absolute; left: 29px; top: 85px; width: 330px; display: grid; grid-template-columns: 169px 161px; }
  .text-block { font-size: 8.8px; line-height: 11.2px; margin-bottom: 4px; white-space: nowrap; }
  .text-block.gap { margin-top: 40px; }
  .page--inside-a .brand, .page--inside-b .brand { left: 34px; top: 514px; }

  /* back */
  .page--back .brand { left: 51px; top: 33px; font-size: 20px; }
  .page--back .brand__dot { width: 22px; height: 22px; }
  .feature-box { position: absolute; left: 27px; top: 114px; width: 322px; height: 133px; background: rgba(10, 30, 18, 0.35); color: var(--white); }
  .feature-box__title { position: absolute; left: 14px; top: 9px; font-size: 17px; font-weight: 700; letter-spacing: 0.6px; }
  .feature-box__text { position: absolute; left: 14px; top: 51px; font-size: 10.5px; line-height: 11.4px; letter-spacing: 0.3px; white-space: nowrap; }
</style>
</head>
<body>
<div class="backdrop"></div>

<!-- Cover -->
<section class="page page--cover">
  <svg class="art" viewBox="0 0 378 537">
    <defs>
      <linearGradient id="coverPhoto" x1="0" y1="0" x2="0.6" y2="1">
        <stop offset="0" stop-color="#c9c91f"/>
        <stop offset="0.3" stop-color="#3a4a2c"/>
        <stop offset="1" stop-color="#17261d"/>
      </linearGradient>
      <linearGradient id="coverFoot" x1="0" y1="0" x2="0" y2="1">
        <stop offset="0" stop-color="#15522a"/>
        <stop offset="1" stop-color="#6a9474"/>
      </linearGradient>
    </defs>
    <rect role="img" aria-label="Photo of yellow paper documents on a dark desk" width="378" height="537" fill="url(#coverPhoto)"/>
    <path d="M0 63 Q120 30 231 50 L231 356 L0 356 Z" fill="var(--earth)"/>
    <path d="M231 50 Q300 60 378 120 L378 0 L231 0 Z" fill="#d6d72a" opacity="0.5"/>
    <rect x="89" y="219" width="282" height="282" fill="var(--panel-green)" opacity="0.95"/>
    <path d="M0 424 Q210 395 378 537 L0 537 Z" fill="var(--olive)"/>
    <path d="M0 453 Q200 430 378 537 L0 537 Z" fill="url(#coverFoot)"/>
  </svg>
  <h1 class="cover-title"><span class="cover-title__main">MAIN</span><span class="cover-title__sub">TEXT</span></h1>
  <p class="cover-intro">Lorem ipsum dolor sit amet, consec-<br>tetur adipiscing elit, sed do eiusmod<br>tempor incididunt ut labore et dolore<br>magna aliqua. Quis ipsum suspendis-<br>se ultrices gravida. Risus commodo<br>viverra maecenas accumsan lacus ve</p>
  <div class="brand"><span class="brand__dot"></span>lumenora</div>
</section>

<!-- Inside page A -->
<section class="page page--inside-a">
  <svg class="art" viewBox="0 0 378 537">
    <polygon points="34,20 283,20 304,53 34,53" fill="#8a8a8a" opacity="0.6"/>
    <polygon points="32,18 281,18 302,51 32,51" fill="var(--olive)"/>
    <polygon points="317,12 355,37 296,37" fill="var(--olive)"/>
    <polygon points="281,18 317,12 305,51" fill="var(--forest)"/>
    <path d="M0 487 Q200 440 378 537 L0 537 Z" fill="var(--olive)"/>
    <path d="M0 509 Q200 470 378 537 L0 537 Z" fill="var(--forest)"/>
  </svg>
  <h2 class="section-title">Lorem Ipsum</h2>
  <div class="columns">
    <div>
      <p class="text-block">Lorem ipsum dolor sit amet, consec-<br>tetur adipiscing elit, sed do eiusmod<br>tempor incididunt ut labore et dolore<br>magna aliqua. Quis ipsum suspendis-<br>se ultrices gravida. Risus commodo<br>viverra maecenas accumsan lacus vel<br>facilisis.</p>
      <p class="text-block">Lorem ipsum dolor sit amet, consec-<br>tetur adipiscing elit, sed do eiusmod<br>tempor incididunt ut labore et dolore<br>magna aliqua. Quis ipsum suspendis-<br>se ultrices gravida. Risus commodo<br>viverra maecenas accumsan lacus vel<br>facilisis.</p>
      <p class="text-block gap">Lorem ipsum dolor sit amet, consec-<br>tetur adipiscing elit, sed do eiusmod<br>tempor incididunt ut labore et dolore<br>magna aliqua. Quis ipsum suspendis-<br>se ultrices gravida. Risus commodo<br>viverra maecenas accumsan lacus vel<br>facilisis.</p>
      <p class="text-block">Lorem ipsum dolor sit amet, consec-<br>tetur adipiscing elit, sed do eiusmod<br>tempor incididunt ut labore et dolore<br>magna aliqua. Quis ipsum suspendis-<br>se ultrices gravida. Risus commodo<br>viverra maecenas accumsan lacus vel<br>facilisis.</p>
    </div>
    <div>
      <p class="text-block">Lorem ipsum dolor sit amet, consec-<br>tetur adipiscing elit, sed do eiusmod<br>tempor incididunt ut labore et dolore<br>magna aliqua. Quis ipsum suspendis-<br>se ultrices gravida. Risus commodo<br>viverra maecenas accumsan lacus vel<br>facilisis.</p>
      <p class="text-block">Lorem ipsum dolor sit amet, consec-<br>tetur adipiscing elit, sed do eiusmod<br>tempor incididunt ut labore et dolore<br>magna aliqua. Quis ipsum suspendis-<br>se ultrices gravida. Risus commodo<br>viverra maecenas accumsan lacus vel<br>facilisis.</p>
      <p class="text-block gap">Lorem ipsum dolor sit amet, consec-<br>tetur adipiscing elit, sed do eiusmod<br>tempor incididunt ut labore et dolore<br>magna aliqua. Quis ipsum suspendis-<br>se ultrices gravida. Risus commodo<br>viverra maecenas accumsan lacus vel<br>facilisis.</p>
      <p class="text-block">Lorem ipsum dolor sit amet, consec-<br>tetur adipiscing elit, sed do eiusmod<br>tempor incididunt ut labore et dolore<br>magna aliqua. Quis ipsum suspendis-<br>se ultrices gravida. Risus commodo<br>viverra maecenas accumsan lacus vel<br>facilisis.</p>
    </div>
  </div>
  <div class="brand"><span class="brand__dot"></span>lumenora</div>
</section>

<!-- Inside page B -->
<section class="page page--inside-b">
  <svg class="art" viewBox="0 0 378 537">
    <polygon points="34,20 283,20 304,53 34,53" fill="#8a8a8a" opacity="0.6"/>
    <polygon points="32,18 281,18 302,51 32,51" fill="var(--olive)"/>
    <polygon points="317,12 355,37 296,37" fill="var(--olive)"/>
    <polygon points="281,18 317,12 305,51" fill="var(--forest)"/>
    <path d="M0 480 Q210 450 378 537 L0 537 Z" fill="var(--olive)"/>
    <path d="M0 496 Q210 480 378 537 L0 537 Z" fill="var(--forest)"/>
  </svg>
  <h2 class="section-title">Lorem Ipsum</h2>
  <div class="columns">
    <div>
      <p class="text-block">Lorem ipsum dolor sit amet, consec-<br>tetur adipiscing elit, sed do eiusmod<br>tempor incididunt ut labore et dolore<br>magna aliqua. Quis ipsum suspendis-<br>se ultrices gravida. Risus commodo<br>viverra maecenas accumsan lacus vel<br>facilisis.</p>
      <p class="text-block">Lorem ipsum dolor sit amet, consec-<br>tetur adipiscing elit, sed do eiusmod<br>tempor incididunt ut labore et dolore<br>magna aliqua. Quis ipsum suspendis-<br>se ultrices gravida. Risus commodo<br>viverra maecenas accumsan lacus vel<br>facilisis.</p>
      <p class="text-block gap">Lorem ipsum dolor sit amet, consec-<br>tetur adipiscing elit, sed do eiusmod<br>tempor incididunt ut labore et dolore<br>magna aliqua. Quis ipsum suspendis-<br>se ultrices gravida. Risus commodo<br>viverra maecenas accumsan lacus vel<br>facilisis.</p>
      <p class="text-block">Lorem ipsum dolor sit amet, consec-<br>tetur adipiscing elit, sed do eiusmod<br>tempor incididunt ut labore et dolore<br>magna aliqua. Quis ipsum suspendis-<br>se ultrices gravida. Risus commodo<br>viverra maecenas accumsan lacus vel<br>facilisis.</p>
    </div>
    <div>
      <p class="text-block">Lorem ipsum dolor sit amet, consec-<br>tetur adipiscing elit, sed do eiusmod<br>tempor incididunt ut labore et dolore<br>magna aliqua. Quis ipsum suspendis-<br>se ultrices gravida. Risus commodo<br>viverra maecenas accumsan lacus vel<br>facilisis.</p>
      <p class="text-block">Lorem ipsum dolor sit amet, consec-<br>tetur adipiscing elit, sed do eiusmod<br>tempor incididunt ut labore et dolore<br>magna aliqua. Quis ipsum suspendis-<br>se ultrices gravida. Risus commodo<br>viverra maecenas accumsan lacus vel<br>facilisis.</p>
      <p class="text-block gap">Lorem ipsum dolor sit amet, consec-<br>tetur adipiscing elit, sed do eiusmod<br>tempor incididunt ut labore et dolore<br>magna aliqua. Quis ipsum suspendis-<br>se ultrices gravida. Risus commodo<br>viverra maecenas accumsan lacus vel<br>facilisis.</p>
      <p class="text-block">Lorem ipsum dolor sit amet, consec-<br>tetur adipiscing elit, sed do eiusmod<br>tempor incididunt ut labore et dolore<br>magna aliqua. Quis ipsum suspendis-<br>se ultrices gravida. Risus commodo<br>viverra maecenas accumsan lacus vel<br>facilisis.</p>
    </div>
  </div>
  <div class="brand"><span class="brand__dot"></span>lumenora</div>
</section>

<!-- Back page -->
<section class="page page--back">
  <svg class="art" viewBox="0 0 378 537">
    <defs>
      <linearGradient id="backPhoto" x1="0" y1="0" x2="1" y2="1">
        <stop offset="0" stop-color="#245c36"/>
        <stop offset="0.55" stop-color="#1f5030"/>
        <stop offset="1" stop-color="#4a8060"/>
      </linearGradient>
    </defs>
    <rect role="img" aria-label="Photo of green tinted stationery and folded papers" width="378" height="537" fill="url(#backPhoto)"/>
  </svg>
  <div class="brand"><span class="brand__dot"></span>lumenora</div>
  <div class="feature-box">
    <h2 class="feature-box__title">Lorem Ipsum</h2>
    <p class="feature-box__text">Lorem ipsum dolor sit amet, consectetur ad-<br>ipiscing elit, sed do eiusmod tempor incidi-<br>dunt ut labore et dolore magna aliqua. Quis<br>ipsum suspendisse ultrices gravida. Risus<br>commodo viverra maecenas accumsan lacus<br>vel facilisis.</p>
  </div>
</section>
</body>
</html>
```